Casa Vero Inspections Business Card

I need a business card for my new company. The company is going to provide home inspections. The name of the company is Casa Vero Inspections. I am not sure if I want a single sided card or a double. I have a logo already that I want to incorporate into the card design. I was wondering if I should incorporate a catch phrase on my card or not. If I did the phrase would be "The Intelligent Choice for Home Inspections" but i am unsure how or if to use it on a card. The following information needs to be on the card.
Home Inspection
My Name: Marcus T. Wolford Phone Number: 555-301-7762 Email: mwolford@casaveroinspections.com Website: www.casaveroinspections.com NY HI License # 27300519462

```html
<!DOCTYPE html>
<html lang="en">
<head>
<meta charset="utf-8">
<title>Casa Vero Inspections Business Card</title>
<link href="https://fonts.googleapis.com/css2?family=Manrope:wght@500;600;700;800&display=swap" rel="stylesheet">
<style>
  :root {
    --backdrop: #d3d4d6;
    --card-dark: #1a1a1a;
    --card-light: #ffffff;
    --brand-blue: #0566a6;
    --sky-blue: #6fc0f0;
    --text-white: #ffffff;
  }
  * { margin: 0; padding: 0; box-sizing: border-box; }
  html, body {
    width: 900px; height: 1200px; overflow: hidden;
    background: var(--backdrop);
    font-family: "Manrope", sans-serif;
  }
  .canvas { position: relative; width: 900px; height: 1200px; }

  .card {
    position: absolute; left: 136px; width: 630px; height: 358px;
    border-radius: 12px; overflow: hidden;
  }

  /* Front */
  .card-front { top: 215px; background: var(--card-dark); }
  .front-brand {
    position: absolute; left: 0; right: 0; top: 170px;
    display: flex; justify-content: center; align-items: center; gap: 14px;
  }
  .front-brand .mark { width: 22px; height: 22px; background: var(--sky-blue); }
  .front-brand .name {
    font-size: 38px; font-weight: 800; color: var(--text-white);
    letter-spacing: 0.5px;
  }
  .tagline {
    position: absolute; left: 0; right: 0; top: 311px;
    text-align: center; font-size: 15px; font-weight: 700;
    color: var(--text-white); letter-spacing: 0.2px;
  }
  .tagline .accent { color: var(--sky-blue); }

  /* Back */
  .card-back { top: 628px; background: var(--card-light); }
  .card-back .band { position: absolute; left: 0; top: 0; }
  .badge {
    position: absolute; left: 332px; top: 53px; width: 256px; height: 256px;
    border-radius: 50%; background: var(--card-light);
    border: 3px solid var(--brand-blue);
    display: flex; align-items: center; justify-content: center;
  }
  .badge .name {
    font-size: 27px; font-weight: 800; color: var(--brand-blue);
    text-align: center; line-height: 1.15; width: 200px;
  }
  .holder { position: absolute; left: 40px; top: 55px; color: var(--text-white); }
  .holder .person { font-size: 24px; font-weight: 700; letter-spacing: -0.2px; }
  .holder .role { font-size: 15px; font-weight: 600; color: var(--sky-blue); margin-top: 2px; }

  .contacts { position: absolute; left: 40px; top: 174px; list-style: none; }
  .contacts li {
    display: flex; align-items: center; gap: 9px;
    height: 23.5px; font-size: 15px; font-weight: 500; color: var(--text-white);
  }
  .contacts li.phone { font-weight: 700; letter-spacing: 3px; }
  .contacts svg { width: 16px; height: 16px; flex: none; }

  .license {
    position: absolute; left: 40px; top: 283px;
    font-size: 15px; font-weight: 700; color: var(--text-white); letter-spacing: 0.3px;
  }
</style>
</head>
<body>
<main class="canvas">

  <section class="card card-front">
    <div class="front-brand">
      <span class="mark"></span>
      <span class="name">Casa Vero Inspections</span>
    </div>
    <p class="tagline">The Intelligent Choice for Home <span class="accent">Inspections</span></p>
  </section>

  <section class="card card-back">
    <svg class="band" width="630" height="358" viewBox="0 0 630 358">
      <rect x="-140" y="22" width="620" height="317" rx="112" fill="var(--sky-blue)"/>
      <rect x="-140" y="26" width="616" height="309" rx="108" fill="var(--card-light)"/>
      <rect x="-140" y="29" width="610" height="303" rx="104" fill="var(--brand-blue)"/>
    </svg>

    <div class="holder">
      <p class="person">Marcus T. Wolford</p>
      <p class="role">President</p>
    </div>

    <ul class="contacts">
      <li class="phone">
        <svg viewBox="0 0 24 24"><path fill="var(--sky-blue)" d="M6.6 10.8a15.1 15.1 0 0 0 6.6 6.6l2.2-2.2c.3-.3.7-.4 1-.2 1.1.4 2.3.6 3.6.6.6 0 1 .4 1 1V20c0 .6-.4 1-1 1A17 17 0 0 1 3 4c0-.6.4-1 1-1h3.5c.6 0 1 .4 1 1 0 1.3.2 2.5.6 3.6.1.3 0 .7-.2 1z"/></svg>
        555-301-7762
      </li>
      <li>
        <svg viewBox="0 0 24 24"><rect x="2" y="5" width="20" height="14" rx="1" fill="var(--sky-blue)"/><path d="M2.5 5.5 12 13l9.5-7.5M2.5 18.5l7-6.5M21.5 18.5l-7-6.5" fill="none" stroke="var(--brand-blue)" stroke-width="1.5"/></svg>
        mwolford@casaveroinspections.com
      </li>
      <li>
        <svg viewBox="0 0 24 24" fill="none" stroke="var(--sky-blue)" stroke-width="1.6"><circle cx="12" cy="12" r="9"/><ellipse cx="12" cy="12" rx="4" ry="9"/><path d="M3 12h18M5 7h14M5 17h14"/></svg>
        www.casaveroinspections.com
      </li>
    </ul>

    <p class="license">NY HI License # 27300519462</p>

    <div class="badge">
      <span class="name">Casa Vero Inspections</span>
    </div>
  </section>

</main>
</body>
</html>
```